New Website for Asia Travel Agency

Lanternpath Journeys Website

We want a redesign for our current website, www.lanternpathjourneys.example. We want you to get creative with our brand and present our company in a unique, creative and compelling way, that communicates our exotic destinations and tours, the local and authentic character of our travel consultants and the trustworthy and professional nature of our company.

Who is this company?

Lanternpath Journeys is an online tour operator specializing in providing tailor-made tours to eight destinations in Asia; Vietnam, Thailand, Laos, Cambodia, Indonesia, Myanmar, Japan and China. They were launched in mid February 2012 with headquarters in Bangkok, Thailand, and staffed by locals and expats with many years of experience in the travel industry, and who are committed to sharing their deep knowledge of, and passion for the region.

Local knowledge

Our consultants at Lanternpath Journeys are all locals – they know their destinations inside-out and draw upon invaluable first-hand experience and information when planning your tour. They have insights into local culture and tradition, they know the best places to visit, the most worthwhile experiences to have and, most importantly, they have the knowledge to create exactly the holiday you desire.

All hotels and activities featured in a Lanternpath Journeys tour are regularly inspected by our consultants to ensure the highest quality standards are met and that all information is correct and up to date.

Unforgettable Travel Experiences

Whether it's a cultural exploration or a beach holiday you're after – or a mix of both – Lanternpath Journeys has an itinerary for you – and if we don't have one, we'll tailor-make one! From the main sights to remote villages, our locally based Travel Specialists will give you unique insights into every place you visit and let you delve into known destinations from new perspectives.

Our tours offer a variety of hotel and resort options, premium stays in deluxe accommodation, heritage hotels, a five-star boutique or on the water in a junk. Tap into our experience let us create an experience unique to you – and one you will never forget.

What type of Holiday to Asia?

Our itineraries at Lanternpath Journeys are created according to different inspirations. Some travelers are interested in the History & Culture of a destination, while some like to stay active with Adventure tours. A Cross Border trip explores different countries in a single tour, while Velvet Summit tours offer the highest level of exclusivity across our destinations. There are 14 different Holiday Types to choose from, or you can mix and match ideas to create your dream vacation.

Target Market(s)

Slightly more female, aged 30-65, are creative, professional and looking for something different, something a bit unusual.

Industry/Entity Type

Boutique

Requirements
Must have
• 5 page designs:

1. Homepage
2. Tours list page for a country
3. Tour page
4. 'Be Inspired' page
5. Country page
6. Enquiry page

Our inspirations.

The following list shows websites we love and which inspire us... to give you some indication of our preferred styles, functions and layouts:

http://www.frostmeridian.example/en/ (we really like this, great personality, like the use of icons for tour types)
http://www.pebblewalks.example.uk/ (very simple design elements and layout)
http://www.sunvalecoast.example/ (great use of background image, nice simple nav bar)
http://www.roamcedarfall.example/ (we like because it has distinct personality and is well suited to the destination)
http://www.seemarlowton.example/ (clear personality through font use)
http://www.vastroving.example/ (original, unique)
http://www.wanderquill.example/long-loop-of-asia (like the map style)

Key design points:

1. You must use our existing logo (attached), but you can change the color scheme of the logo to accord with the whichever color scheme you choose for the main designs.
2. Our logo strapline is "Asia is our Lanternpath" and should be used prominently on the page to reinforce the meaning of our company name.
3. Home page and tours list pages should allow the user to see the choice of tours immediately without scrolling & Introduction copy should be minimal.
4. We and our site visitors are inspired and excited by our photography, this is an element of the site which we would like to maintain and build on, though the section page header sliders are currently too big and do not allow quick access to the section content. This is a design problem which needs a solution. Full page photographic backgrounds may be an answer?
5. Tour page should display other contextual tours, from the same country or style/type
6. We should promote press coverage in various places
7. We should display consultant profiles in various places
8. Map designs for tour page and country page, plus a modal pop out for the home page. These are complex and may have a few small photos and short descriptive text only, though this is limited by your own creativity. We will use graphics and html5/css3 so there are no creative limitations.
9. The 'Inspirations' / 'Be Inspired' page is for people who want travel and holiday ideas, who are looking for inspiration on where to go and what to do. This section needs to reflect the exotic, the unusual, the extraordinary in our destinations and tours, and we leave this to your creative genius to develop. We are also interested in how this inspirations page is related to the blog and social media content we produce daily, is there an integration here? Can we present YouTube videos, our blog posts, Facebook posts etc, on this page? This is another design challenge.
10. We would like to see designs for the tours list page which feature AJAX content filtering (for instance: http://demo.layoutbrisk.example/?acn), we would like to see how to include this type of content filtering on homepage and destination page also.
11. The 'Enquiry' call to action should be on all pages and prominent.
12. The enquiry page can reflect the same fields as the existing website enquiry page

Values to be communicated:

- Exotic: Asia is exotic, and our tours will expose clients to extraordinary sights and unusual cultural encounters.
- Authentic: Our travel consultants all live in the destinations themselves, they are local nationals and have all the insider knowledge to give clients a truly authentic experience of our destinations
- Unique: All of our tours are tailor made, there are no fixed departure dates or join-in groups. All tour itineraries can be uniquely designed for our clients, from departure dates to destinations.
- Trust: Some travelers prefer to book their holidays with local agencies they can meet in person, rather than with online companies like us who live in the destinations and who they only get to meet on Skype video or phone. We want to convey that we are trustworthy. We have attempted this through presenting a 'meet the team' page and a 'press' page and advert, as well as offering a prominent international phone number. How we you build on this and further convey this value?

```html
<!DOCTYPE html>
<html lang="en">
<head>
<meta charset="utf-8">
<title>Lanternpath Journeys – Asia is our Lanternpath</title>
<link href="https://fonts.googleapis.com/css2?family=Open+Sans:ital,wght@0,400;0,600;0,700;1,400&display=swap" rel="stylesheet">
<style>
:root{
  --teal:#3db0a5;
  --teal-dark:#2e978c;
  --ink:#363636;
  --text:#555;
  --muted:#8a8480;
  --page:#ebe6e1;
  --band:#d4cac1;
  --nav:#c3b6ac;
  --tan:#b5a89d;
  --gold:#f4b707;
  --line:#d8d1cb;
  --white:#fff;
  --panel:rgba(72,56,44,.82);
}
*{box-sizing:border-box;margin:0;padding:0}
html,body{width:1200px;height:2542px;overflow:hidden}
body{position:relative;background:var(--page);font-family:"Open Sans",Arial,sans-serif;color:var(--text);font-size:12px}
.abs{position:absolute}

/* header */
.site-header{position:absolute;top:0;left:0;width:1200px;height:74px;background:var(--white)}
.brand{position:absolute;left:95px;top:12px;display:flex;align-items:center;gap:10px}
.brand-mark{width:40px;height:40px;background:#9aa3a6;border-radius:6px}
.brand-name{font-size:20px;font-weight:700;color:var(--ink);line-height:22px}
.brand-strap{font-size:11px;font-weight:700;color:var(--ink);margin-left:38px;line-height:14px}
.call{position:absolute;left:572px;top:18px;display:flex;gap:9px;align-items:center}
.call-icon{width:28px;height:28px;border-radius:50%;background:var(--teal);display:flex;align-items:center;justify-content:center}
.call-label{font-size:9.5px;font-weight:700;color:#777;line-height:12px}
.call-number{font-size:14px;font-weight:700;color:#666;line-height:17px}
.site-search{position:absolute;left:790px;top:22px;width:240px;height:30px;border:1px solid #cfcfcf;border-radius:15px;padding:0 12px;display:flex;align-items:center;justify-content:space-between;font-size:11px;color:#888}
.account-ribbon{position:absolute;left:1047px;top:0;width:94px;height:132px;background:var(--teal);clip-path:polygon(0 0,100% 0,100% 100%,50% 88%,0 100%);display:flex;flex-direction:column;align-items:center;padding-top:10px}
.account-ribbon span{color:var(--white);font-size:10.5px;font-weight:600;height:36px;line-height:36px;width:100%;text-align:center;border-bottom:1px solid rgba(255,255,255,.25)}
.account-ribbon span:first-child{height:26px;line-height:18px}
.account-ribbon span:last-child{border:0}

.main-nav{position:absolute;top:74px;left:0;width:1200px;height:31px;background:var(--nav)}
.main-nav a{position:absolute;top:0;height:31px;line-height:31px;font-size:11px;color:var(--white);text-decoration:none;text-transform:uppercase;letter-spacing:.2px}
.main-nav a.active{background:#ebe6e1;color:#555;padding:0 18px;top:5px;height:21px;line-height:21px;font-weight:600}

/* hero */
.hero-photo{position:absolute;top:105px;left:0;width:1200px;height:524px;background:linear-gradient(180deg,#5f84b0 0%,#9db8d4 18%,#d9e2e6 34%,#b9c3b9 46%,#6f8d4a 60%,#45622b 78%,#2f4620 100%)}
.hero-band{position:absolute;top:629px;left:0;width:1200px;height:100px;background:var(--band)}
.tours-panel{position:absolute;left:831px;top:216px;width:308px;height:290px;background:var(--panel)}
.tours-panel h3{position:absolute;left:22px;top:8px;font-size:12px;font-weight:700;color:var(--white)}
.thumb{position:absolute;width:80px;height:50px;border:2px solid #f1ece7}
.thumb-label{position:absolute;width:90px;text-align:center;font-size:9.5px;color:var(--white);text-transform:uppercase}
.tours-panel .more{position:absolute;left:0;width:100%;top:270px;text-align:center;font-size:11px;color:var(--white)}

/* search */
.finder{position:absolute;left:57px;top:532px;width:1085px;height:155px;background:var(--white);border:3px solid #d0d0d0}
.finder .q{position:absolute;top:17px;font-size:14px;color:#555}
.finder .sub{position:absolute;top:53px;font-size:11px;color:#666}
.finder .divider{position:absolute;top:50px;width:1px;height:72px;background:var(--line)}
.field{position:absolute;top:74px;height:30px;border:1px solid #c9c9c9;border-radius:15px;font-size:10.5px;color:#888;padding:0 12px;display:flex;align-items:center;justify-content:space-between}
.radio{position:absolute;display:flex;gap:6px;align-items:center;font-size:11px;color:#555}
.radio i{display:block;width:15px;height:15px;border:1px solid #aaa;border-radius:50%;position:relative}
.radio i.on::after{content:"";position:absolute;left:3px;top:1px;width:5px;height:8px;border:solid #444;border-width:0 2px 2px 0;transform:rotate(40deg)}
.proceed{position:absolute;left:524px;top:654px;width:174px;height:30px;background:var(--teal);border-radius:15px 15px 0 0;color:var(--white);font-size:10.5px;font-weight:700;text-align:center;line-height:30px;box-shadow:0 2px 0 var(--teal-dark)}

/* intro */
.intro{position:absolute;left:57px;top:757px;width:812px}
.intro h1{font-size:29px;font-weight:600;color:#6b6864;margin-bottom:14px}
.intro p{font-size:11.6px;line-height:19.4px;color:#444;margin-bottom:12px}
.testimonial{position:absolute;left:886px;top:762px;width:255px;height:211px;background:var(--white);border:1px solid #cdc6c0;box-shadow:inset 0 0 0 6px #f3f0ed}
.testimonial .quote-mark{position:absolute;left:16px;top:2px;font-size:44px;color:#d8d4d0;font-family:Georgia,serif}
.testimonial h4{position:absolute;left:52px;top:30px;font-size:13px;font-weight:400;color:#666}
.testimonial p{position:absolute;left:36px;top:56px;width:200px;font-size:11.5px;line-height:15px;color:#555}
.testimonial .who{position:absolute;left:46px;top:146px;width:120px;font-size:8px;font-style:italic;color:#777;text-transform:uppercase;text-align:right;line-height:11px}
.portrait{position:absolute;left:172px;top:124px;width:60px;height:70px;border:2px solid #ddd;background:linear-gradient(160deg,#7d7d7d,#2b2b2b)}

/* tabs & cards */
.tab{position:absolute;top:1015px;height:41px;width:255px;line-height:41px;text-align:center;font-size:17px}
.tab-hot{left:57px;background:var(--teal);color:var(--white)}
.tab-new{left:332px;background:#c8c8c8;color:#666}
.pager{position:absolute;display:flex;align-items:center;gap:6px;font-size:14px;color:#444}
.pager b{background:var(--teal);color:var(--white);width:18px;height:18px;text-align:center;line-height:18px;font-weight:600;font-size:13px}
.pager .arrows{margin-left:26px;font-weight:700;letter-spacing:4px;font-size:15px}
.card-row{position:absolute;left:57px;display:grid;grid-template-columns:repeat(4,255px);column-gap:22px}
.card{background:var(--white);position:relative;box-shadow:0 1px 2px rgba(0,0,0,.06)}
.card .photo{height:144px}
.dest-card{height:252px}
.dest-card h3{font-size:13px;font-weight:400;color:#444;margin:20px 18px 0;padding-bottom:10px;border-bottom:1px solid #e2ddd8}
.pill{display:block;width:140px;height:27px;margin:21px auto 0;background:var(--teal);color:var(--white);border-radius:14px;font-size:9.5px;font-weight:700;text-align:center;line-height:27px;text-transform:uppercase}
.section-rule{position:absolute;left:57px;width:1085px;height:1px;background:#cfc7c0}
.section-title{position:absolute;left:57px;font-size:18px;font-weight:700;color:#333}
.promo-card{height:273px}
.promo-card .tag{position:absolute;left:26px;top:0;width:50px;height:52px;clip-path:polygon(0 0,100% 0,100% 100%,50% 78%,0 100%);color:var(--white);font-size:14px;font-weight:600;text-align:center;padding-top:12px}
.tag-teal{background:var(--teal)}
.tag-gold{background:var(--gold)}
.promo-card h3{position:absolute;left:18px;top:160px;width:120px;font-size:12.5px;font-weight:400;color:#333;line-height:16px}
.promo-card .view{position:absolute;right:12px;top:162px;width:100px;height:28px;border-radius:14px;background:var(--teal);color:var(--white);font-size:9.5px;font-weight:700;text-align:center;line-height:28px}
.promo-card .duration{position:absolute;left:0;top:216px;width:100%;height:43px;background:var(--tan);color:var(--white);font-size:14.5px;text-align:center;line-height:43px}
.promo-card .duration.gold{background:var(--gold)}

/* features */
.feature-grid{position:absolute;left:57px;top:1776px;display:grid;grid-template-columns:repeat(4,255px);grid-template-rows:159px 179px;gap:22px}
.feature{background:linear-gradient(180deg,#fff 0%,#f1efed 100%);border:1px solid #e0dad4;padding:14px 16px;position:relative}
.feature h4{font-size:13.5px;font-weight:700;color:var(--teal);margin-bottom:18px}
.feature h4 em{font-style:normal;color:#444}
.feature .icon{position:absolute;right:18px;top:12px}
.feature p{font-size:11.2px;line-height:16.6px;color:#6d6965}
.feature .more{display:block;text-align:center;font-size:11px;color:#444;margin-top:6px}

/* countries */
.flag{position:absolute;width:44px;height:28px}
.country{position:absolute;font-size:15px;color:#333;letter-spacing:.8px}
.explore{position:absolute;left:482px;top:2278px;width:251px;height:39px;background:var(--teal);border:3px solid #bfe2de;color:var(--white);font-size:18px;display:flex;align-items:center;justify-content:center;gap:10px}

/* footer */
.site-footer{position:absolute;left:0;top:2345px;width:1200px;height:197px;background:var(--white)}
.site-footer h5{position:absolute;top:22px;font-size:15px;font-weight:700;color:#333}
.site-footer h5 span{font-weight:400;color:#555}
.foot-text{position:absolute;font-size:11.5px;line-height:21px;color:#333}
.foot-text strong{font-weight:700}
.foot-text .hl{color:var(--teal);font-weight:700}
.foot-list{position:absolute;left:334px;top:56px;list-style:none;font-size:11px;line-height:19.5px;color:#666}
.foot-list li::before{content:"• ";color:#999}
.socials{position:absolute;left:580px;top:58px;display:flex;gap:4px}
.socials i{width:27px;height:27px;border-radius:50%;background:#cdbfb4;display:block}
.news-note{position:absolute;left:886px;top:54px;width:256px;font-size:9.5px;line-height:13px;color:#777}
.news-input{position:absolute;left:886px;top:92px;width:192px;height:30px;border:1px solid #ccc;border-radius:15px 0 0 15px;font-size:11px;color:#888;padding-left:12px;line-height:28px}
.news-btn{position:absolute;left:1074px;top:92px;width:67px;height:30px;background:var(--teal);border-radius:0 15px 15px 0;color:var(--white);font-size:9.5px;font-weight:700;text-align:center;line-height:30px}
.foot-bar{position:absolute;left:57px;top:161px;width:1085px;border-top:1px solid #e4e0dc;padding-top:10px;display:flex;justify-content:space-between;font-size:11px;color:#555}
.foot-bar nav span{margin-left:10px}
.foot-bar nav span.sep{margin-left:10px;color:#aaa}
</style>
</head>
<body>

<header class="site-header">
  <div class="brand">
    <div class="brand-mark"></div>
    <div>
      <div class="brand-name">Lanternpath Journeys</div>
      <div class="brand-strap">Asia is our Lanternpath.</div>
    </div>
  </div>
  <div class="call">
    <div class="call-icon">
      <svg width="14" height="14" viewBox="0 0 24 24"><path fill="#fff" d="M6.6 10.8c1.4 2.8 3.8 5.1 6.6 6.6l2.2-2.2c.3-.3.7-.4 1-.2 1.1.4 2.3.6 3.6.6.6 0 1 .4 1 1V20c0 .6-.4 1-1 1C10.6 21 3 13.4 3 4c0-.6.4-1 1-1h3.5c.6 0 1 .4 1 1 0 1.3.2 2.5.6 3.6.1.3 0 .7-.2 1z"/></svg>
    </div>
    <div>
      <div class="call-label">+( INTERNATIONAL CALLS )</div>
      <div class="call-number">+800-4417-3862</div>
    </div>
  </div>
  <div class="site-search">
    <span>Search entire site here</span>
    <svg width="13" height="13" viewBox="0 0 24 24"><circle cx="10" cy="10" r="7" fill="none" stroke="#999" stroke-width="2.5"/><path d="M15 15l6 6" stroke="#999" stroke-width="2.5"/></svg>
  </div>
  <div class="account-ribbon">
    <span>MY ACCOUNT</span>
    <span>ENGLISH (US)</span>
    <span>$ US DOLLAR</span>
  </div>
</header>

<nav class="main-nav">
  <a class="active" style="left:44px">Home</a>
  <a style="left:140px">Destinations</a>
  <a style="left:273px">Tours</a>
  <a style="left:358px">Holiday Types</a>
  <a style="left:490px">Best Values</a>
  <a style="left:614px">About Us</a>
  <a style="left:723px">Blog</a>
</nav>

<div class="hero-photo" role="img" aria-label="Great Wall of China winding along green mountain ridges above a sea of morning mist"></div>
<div class="hero-band"></div>

<aside class="tours-panel">
  <h3>TOURS »</h3>
  <div class="thumb" style="left:22px;top:33px;background:linear-gradient(#e7a64a,#6a4a7a)" role="img" aria-label="Thai temple at dusk"></div>
  <div class="thumb" style="left:114px;top:33px;background:linear-gradient(#7fa8d8,#c0392b)" role="img" aria-label="Japanese shrine gate on water"></div>
  <div class="thumb" style="left:206px;top:33px;background:linear-gradient(#f2c26b,#8a4b1c)" role="img" aria-label="Myanmar pagodas at sunset"></div>
  <div class="thumb-label" style="left:17px;top:92px">Thailand</div>
  <div class="thumb-label" style="left:109px;top:92px">Japan</div>
  <div class="thumb-label" style="left:201px;top:92px">Myanmar</div>

  <div class="thumb" style="left:22px;top:111px;background:linear-gradient(#88b4df,#b0622e)" role="img" aria-label="Lao temple roof"></div>
  <div class="thumb" style="left:114px;top:111px;background:linear-gradient(#e5c36f,#9b6a2a)" role="img" aria-label="Vietnamese lanterns"></div>
  <div class="thumb" style="left:206px;top:111px;background:linear-gradient(#d74a3a,#5a1a14)" role="img" aria-label="Chinese red lanterns"></div>
  <div class="thumb-label" style="left:17px;top:168px">Laos</div>
  <div class="thumb-label" style="left:109px;top:168px">Vietnam</div>
  <div class="thumb-label" style="left:201px;top:168px">China</div>

  <div class="thumb" style="left:22px;top:186px;background:linear-gradient(#9a9a9a,#4a4a4a)" role="img" aria-label="Cambodian temple stone carvings"></div>
  <div class="thumb" style="left:114px;top:186px;background:linear-gradient(#3a7f4a,#d9453a)" role="img" aria-label="Market stalls across several countries"></div>
  <div class="thumb" style="left:206px;top:186px;background:linear-gradient(#6fb2d6,#2f6f8a)" role="img" aria-label="Indonesian coastline"></div>
  <div class="thumb-label" style="left:17px;top:245px">Cambodia</div>
  <div class="thumb-label" style="left:109px;top:245px">Multi-Coun…</div>
  <div class="thumb-label" style="left:201px;top:245px">Indonesia</div>
  <div class="more">MOST POPULAR TOURS »</div>
</aside>

<section class="finder">
  <div class="q" style="left:118px">What ?</div>
  <div class="q" style="left:242px">Where?</div>
  <div class="q" style="left:517px">When?</div>
  <div class="q" style="left:798px">Who?</div>
  <div class="radio" style="left:92px;top:54px"><i class="on"></i>Hotel Type</div>
  <div class="radio" style="left:92px;top:78px"><i></i>Tours</div>
  <div class="sub" style="left:218px">Your destination</div>
  <div class="field" style="left:218px;width:242px">City, Region, District or specific hotel</div>
  <div class="divider" style="left:478px"></div>
  <div class="sub" style="left:495px">Check-in date</div>
  <div class="sub" style="left:621px">Check-out date</div>
  <div class="field" style="left:493px;width:122px"><span></span><svg width="14" height="13" viewBox="0 0 14 13"><rect x="1" y="2" width="12" height="10" fill="none" stroke="#999"/><path d="M1 5h12M4 0v3M10 0v3" stroke="#999"/></svg></div>
  <div class="field" style="left:619px;width:114px"><span></span><svg width="14" height="13" viewBox="0 0 14 13"><rect x="1" y="2" width="12" height="10" fill="none" stroke="#999"/><path d="M1 5h12M4 0v3M10 0v3" stroke="#999"/></svg></div>
  <div class="divider" style="left:750px"></div>
  <div class="sub" style="left:771px">Rooms</div>
  <div class="sub" style="left:849px">Adults</div>
  <div class="sub" style="left:929px">Children</div>
  <div class="field" style="left:766px;width:74px"><span></span><svg width="8" height="12" viewBox="0 0 8 12"><path d="M1 5l3-4 3 4M1 7l3 4 3-4" fill="none" stroke="#888"/></svg></div>
  <div class="field" style="left:846px;width:72px"><span></span><svg width="8" height="12" viewBox="0 0 8 12"><path d="M1 5l3-4 3 4M1 7l3 4 3-4" fill="none" stroke="#888"/></svg></div>
  <div class="field" style="left:925px;width:72px"><span></span><svg width="8" height="12" viewBox="0 0 8 12"><path d="M1 5l3-4 3 4M1 7l3 4 3-4" fill="none" stroke="#888"/></svg></div>
</section>
<div class="proceed">PROCEED TO RESULTS</div>

<section class="intro">
  <h1>Asia Is Our Lanternpath</h1>
  <p>No one knows a destination better than someone who lives, works and plays there. That's the foundation of Lanternpath Journeys. Lanternpath Journeys is an online tour operator specializing in providing tailor-made tours to eight destinations in Asia; Vietnam, Thailand, Laos, Cambodia, Indonesia, Myanmar, Japan and China. They were launched in mid February 2012 with headquarters in Bangkok, Thailand, and staffed by locals and expats with many years of experience in the travel industry, and who are committed to sharing their deep knowledge of, and passion for the region.</p>
  <p>The result is a travel company tailor-made for the person with a taste for veering off the well-trodden path, for the adventurer who wants access to Asia's most spectacular sights, but hidden charms as well, on the road less traveled.</p>
  <p>Want to explore this Asia? Step into our Lanternpath.</p>
</section>

<aside class="testimonial">
  <div class="quote-mark">“</div>
  <h4>GREAT SUCCESS</h4>
  <p>It was a terrific trip and we are most grateful for the careful attention you gave all our requests.</p>
  <div class="who">Mr. Oliver Quentin Hale</div>
  <div class="portrait" role="img" aria-label="Portrait photo of the traveller"></div>
</aside>

<div class="tab tab-hot">Hot Destinations</div>
<div class="tab tab-new">New Creations</div>
<div class="pager" style="left:1013px;top:1049px"><b>1</b><span>2</span><span>3</span><span class="arrows">‹›</span></div>

<div class="card-row" style="top:1083px">
  <article class="card dest-card">
    <div class="photo" role="img" aria-label="Great Wall over misty blue mountains" style="background:linear-gradient(180deg,#8fb3d6,#d8e0e4 45%,#5f7c4a)"></div>
    <h3>Epic China</h3><span class="pill">Explore our deals</span>
  </article>
  <article class="card dest-card">
    <div class="photo" role="img" aria-label="Fisherman on a boat at golden sunset on a lake" style="background:linear-gradient(180deg,#f3d79a,#d5a05a 55%,#6a4a2a)"></div>
    <h3>The Best Of Myanmar</h3><span class="pill">Explore our deals</span>
  </article>
  <article class="card dest-card">
    <div class="photo" role="img" aria-label="Cyclists riding along a leafy village road" style="background:linear-gradient(180deg,#5d7a3a,#9aa07a 50%,#7a6a58)"></div>
    <h3>Ho Chi Minh Trail Bike Adventure</h3><span class="pill">Explore our deals</span>
  </article>
  <article class="card dest-card">
    <div class="photo" role="img" aria-label="Woman in pink traditional dress holding flowers" style="background:linear-gradient(180deg,#6b8a3a,#d777a8 60%,#b8467e)"></div>
    <h3>Honeymoon In Thailand</h3><span class="pill">Explore our deals</span>
  </article>
</div>

<div class="section-rule" style="top:1372px"></div>
<h2 class="section-title" style="top:1393px">Our Featured Promotions</h2>
<div class="pager" style="left:1013px;top:1416px"><b>1</b><span>2</span><span>3</span><span class="arrows">‹›</span></div>

<div class="card-row" style="top:1449px">
  <article class="card promo-card">
    <div class="photo" role="img" aria-label="Ornate golden temple facade" style="background:linear-gradient(160deg,#caa14a,#7a4a1e 60%,#3a2a18)"></div>
    <div class="tag tag-teal">-15%</div>
    <h3>Discover Bangkok &amp; Angkor Wat</h3><span class="view">VIEW TOUR</span>
    <div class="duration">Duration - 5 Days / 4 Nights</div>
  </article>
  <article class="card promo-card">
    <div class="photo" role="img" aria-label="Stone statue among green leaves" style="background:linear-gradient(160deg,#9cc45a,#4a7a2a 60%,#2a4a18)"></div>
    <div class="tag tag-gold">-15%</div>
    <h3>Quintessential Thailand</h3><span class="view">VIEW TOUR</span>
    <div class="duration gold">Duration - 12 Days / 11 Nights</div>
  </article>
  <article class="card promo-card">
    <div class="photo" role="img" aria-label="Ancient temple ruins with tree roots" style="background:linear-gradient(160deg,#9a9a86,#5a5a48 60%,#3a3a2e)"></div>
    <div class="tag tag-teal">-15%</div>
    <h3>Ancient Empire: Explore Angkor</h3><span class="view">VIEW TOUR</span>
    <div class="duration">Duration - 4 Days / 3 Nights</div>
  </article>
  <article class="card promo-card">
    <div class="photo" role="img" aria-label="Balinese dancer in golden costume" style="background:linear-gradient(160deg,#6fa2b8,#c9a04a 55%,#a8322a)"></div>
    <div class="tag tag-teal">-10%</div>
    <h3>Ubud In Style</h3><span class="view">VIEW TOUR</span>
    <div class="duration">Duration - 4 Days / 3 Nights</div>
  </article>
</div>

<div class="section-rule" style="top:1750px"></div>

<section class="feature-grid">
  <div class="feature">
    <h4>Why <em>Lanternpath Journeys</em></h4>
    <svg class="icon" width="14" height="18" viewBox="0 0 14 18"><text x="1" y="15" font-size="17" font-weight="700" fill="#9a9a9a" font-family="Open Sans,sans-serif">?</text></svg>
    <p>A travel company that's owned and operated by people who live, work &amp; play in Asia.....</p>
    <span class="more">Learn More...</span>
  </div>
  <div class="feature">
    <h4>Handpicked Hotels</h4>
    <svg class="icon" width="18" height="18" viewBox="0 0 18 18"><rect x="2" y="3" width="9" height="14" fill="#9a9a9a"/><rect x="11" y="8" width="5" height="9" fill="#b5b5b5"/><path d="M4 6h2M7 6h2M4 9h2M7 9h2M4 12h2M7 12h2" stroke="#fff"/></svg>
    <p>All Lanternpath Journeys Hotels fulfil strict selection criteria. Each hotel is chosen individually and inclusion cannot be bought.</p>
  </div>
  <div class="feature">
    <h4>Detailed Descriptions</h4>
    <svg class="icon" width="18" height="16" viewBox="0 0 18 16"><path d="M1 2c3-1 6-1 8 1 2-2 5-2 8-1v12c-3-1-6-1-8 1-2-2-5-2-8-1z" fill="none" stroke="#9a9a9a" stroke-width="1.6"/><path d="M9 3v12" stroke="#9a9a9a" stroke-width="1.4"/></svg>
    <p>To give you an accurate impression of the hotel, we endeavor to publish transparent, balanced and precise hotel descriptions.</p>
  </div>
  <div class="feature">
    <h4>Passionate Service</h4>
    <svg class="icon" width="18" height="18" viewBox="0 0 18 18"><circle cx="9" cy="9" r="5" fill="none" stroke="#9a9a9a" stroke-width="3.5" stroke-dasharray="3 2"/><circle cx="9" cy="9" r="2" fill="#9a9a9a"/></svg>
    <p>Lanternpath Journeys's team will cater to your special requests. We offer expert and passionate advice for finding the right hotel.</p>
  </div>
  <div class="feature">
    <h4>Best Price Guarantee</h4>
    <svg class="icon" width="18" height="18" viewBox="0 0 18 18"><circle cx="9" cy="9" r="6" fill="none" stroke="#9a9a9a" stroke-width="3" stroke-dasharray="2 1.6"/><circle cx="9" cy="9" r="3" fill="#9a9a9a"/></svg>
    <p>We offer the best hotels at the best prices. If you find the same room category on the same dates cheaper elsewhere, we will refund the difference. Guaranteed, and quickly.</p>
  </div>
  <div class="feature">
    <h4>Secure Booking</h4>
    <svg class="icon" width="18" height="18" viewBox="0 0 18 18"><circle cx="9" cy="9" r="7.5" fill="#9a9a9a"/><path d="M3 7c3 0 4 2 6 1s2-4 5-3M5 14c1-2 3-2 4-4" stroke="#eee" stroke-width="1.2" fill="none"/></svg>
    <p>Lanternpath Journeys reservation system is secure and your credit card and personal information is encrypted. We work to high standards and guarantee your privacy.</p>
  </div>
  <div class="feature">
    <h4>Press Coverage</h4>
    <svg class="icon" width="20" height="16" viewBox="0 0 20 16"><rect x="1" y="2" width="18" height="12" fill="none" stroke="#9a9a9a" stroke-width="1.6"/><rect x="4" y="5" width="5" height="6" fill="#9a9a9a"/><path d="M11 5h5M11 8h5M11 11h5" stroke="#9a9a9a"/></svg>
    <p>Harbor News Edition - 18 July 2013</p>
    <p style="margin-top:8px">Inside Cambodia's stunning new temple discoveries</p>
    <span class="more">Learn More...</span>
  </div>
  <div class="feature">
    <h4>Any Questions?</h4>
    <svg class="icon" width="10" height="18" viewBox="0 0 10 18"><circle cx="5" cy="3" r="2" fill="#9a9a9a"/><rect x="3.5" y="7" width="3" height="10" fill="#9a9a9a"/></svg>
    <p>Call us on <b style="color:var(--teal)">+800-4417-3862</b> for individual, tailored advice for your perfect stay or send us a message with your hotel booking query.</p>
  </div>
</section>

<!-- destinations row -->
<svg class="flag" style="left:177px;top:2173px" viewBox="0 0 44 28"><rect width="44" height="28" fill="#c8202a"/><rect y="5" width="44" height="18" fill="#fff"/><rect y="9" width="44" height="10" fill="#2d2a6b"/></svg>
<span class="country" style="left:247px;top:2176px">THAILAND</span>
<svg class="flag" style="left:364px;top:2173px" viewBox="0 0 44 28"><rect width="44" height="14" fill="#e0202a"/><rect y="14" width="44" height="14" fill="#f4f4f4"/></svg>
<span class="country" style="left:436px;top:2176px">INDONESIA</span>
<svg class="flag" style="left:563px;top:2173px" viewBox="0 0 44 28"><rect width="44" height="28" fill="#ce2a2a"/><rect y="7" width="44" height="14" fill="#1f3b8a"/><circle cx="22" cy="14" r="5" fill="#fff"/></svg>
<span class="country" style="left:633px;top:2176px">LAOS</span>
<svg class="flag" style="left:707px;top:2173px" viewBox="0 0 44 28"><rect width="44" height="28" fill="#1e3f9a"/><rect y="7" width="44" height="14" fill="#d8262a"/><rect x="16" y="10" width="12" height="8" fill="#fff"/></svg>
<span class="country" style="left:779px;top:2176px">CAMBODIA</span>
<svg class="flag" style="left:903px;top:2173px" viewBox="0 0 44 28"><rect width="44" height="28" fill="#fff" stroke="#ddd"/><circle cx="22" cy="14" r="7" fill="#c8202a"/></svg>
<span class="country" style="left:975px;top:2176px">JAPAN</span>

<span class="country" style="left:247px;top:2226px">MYANMAR</span>
<svg class="flag" style="left:364px;top:2223px" viewBox="0 0 44 28"><rect width="44" height="10" fill="#f4c81a"/><rect y="9" width="44" height="10" fill="#2f9a3a"/><rect y="18" width="44" height="10" fill="#d62a2a"/><path d="M22 5l2.4 7h7.3l-5.9 4.3 2.3 7-6.1-4.4-6.1 4.4 2.3-7-5.9-4.3h7.3z" fill="#fff"/></svg>
<span class="country" style="left:436px;top:2226px">VIETNAM</span>
<svg class="flag" style="left:563px;top:2223px" viewBox="0 0 44 28"><rect width="44" height="28" fill="#d8262a"/><path d="M22 6l2 6h6.3l-5.1 3.7 2 6-5.2-3.7-5.2 3.7 2-6-5.1-3.7H20z" fill="#f6d21a"/></svg>
<span class="country" style="left:633px;top:2226px">CHINA</span>
<svg class="flag" style="left:715px;top:2221px;width:32px;height:32px" viewBox="0 0 32 32"><circle cx="16" cy="16" r="14" fill="#2b5da8"/><path d="M2 16h28M16 2v28M5 8c7 3 15 3 22 0M5 24c7-3 15-3 22 0" stroke="#9fc3ea" stroke-width="1.2" fill="none"/><ellipse cx="16" cy="16" rx="7" ry="14" fill="none" stroke="#9fc3ea" stroke-width="1.2"/></svg>
<span class="country" style="left:779px;top:2226px">MULTI-COUNTRY</span>

<div class="explore">
  <svg width="18" height="18" viewBox="0 0 24 24"><circle cx="10" cy="10" r="7" fill="none" stroke="#fff" stroke-width="3"/><path d="M15 15l6 6" stroke="#fff" stroke-width="3.5"/></svg>
  Explore Asia
</div>

<footer class="site-footer">
  <h5 style="left:57px">Lanternpath Journeys</h5>
  <div class="foot-text" style="left:57px;top:53px">
    <strong>Address Lorem Ipsum is a Dummy Sample</strong><br>
    <span class="hl">P: +International Call: +800-4417-3862</span><br>
    <span class="hl">E: hello@lanternpath.example</span>
  </div>
  <h5 style="left:334px"><span>About</span> Lanternpath Journeys</h5>
  <ul class="foot-list">
    <li>Why Book With Us</li>
    <li>Meet The Team</li>
    <li>Careers</li>
    <li>In The Press</li>
    <li>Affiliate Program</li>
  </ul>
  <h5 style="left:580px">Follow us</h5>
  <div class="socials" aria-label="Social channels"><i></i><i></i><i></i><i></i><i></i><i></i><i></i><i></i><i></i></div>
  <h5 style="left:886px">Don't miss our exclusive offers</h5>
  <p class="news-note">Sign up for Lanternpath Journeys's e-newsletter featuring promotions, travel musings and insider destination tips.</p>
  <div class="news-input">Enter your email here</div>
  <div class="news-btn">SIGNUP</div>
  <div class="foot-bar">
    <span>© 2013 Lanternpath Journeys. All Rights Reserved</span>
    <nav>
      <span>Home</span><span class="sep">/</span><span>Destinations</span><span class="sep">/</span><span>Tours</span><span class="sep">/</span><span>Holiday types</span><span class="sep">/</span><span>Best Value</span><span class="sep">/</span><span>About us</span><span class="sep">/</span><span>Blog</span><span class="sep">/</span><span>Contact Us</span><span class="sep">/</span><span>Terms</span>
    </nav>
  </div>
</footer>

</body>
</html>
```